Full revamp of cheap website design - the best designer will be offered a much larger project!

Tolland Vesper are a progressive and innovative mid-tier professional services group (accountants and business advisors) with offices based in major cities throughout Australia and New Zealand.
Our positioning statement is "Energetic, Innovative, Streetwise", and the visual appearance must reflect this. Although still a relatively conservative industry, we aim to project a modern, innovative, energetic, highly professional but approachable image. The presentation should tie in with the theme "we take our work seriously, not ourselves".
Our aim with this new design is the elevate the status of the group in its online presentation and communication... we want to 'impress' and stand out from the crowd! See our existing site at www.tollandvesper.com.au
We're looking for a special designer to take on the Web Site Design Concept - Uncoded - graphics only in line with the concept architecture we will provide (although we are flexible with the layout - we want an interface design that works!). Must work within the constraints of a suitable wordpress theme... Designer to source (we quite like themoquill.com as an option, but havn't seen any really slick representations of it)... there are many other great themes to choose from). Must include a series of slick flash banner designs.
or alternatively,
Design and coding (custom design theme) using wordpress platform (unless you can convince us of the benefits of using some other recognised and supported platform).
Happy to receive the design concepts as graphics only (but the flash is an important factor). You'll need to prove that it will work within an existing theme (or that you are capable of quickly developing a bug-free custom site on the wordpress platform.
Only highly talented and professional designers need enter, but the right designer will be well rewarded with the offer of a much larger design project and plenty of ongoing work.
Task
We are completely overhauling our existing and outdated website(s) x 9 and are looking for a new visual design concept (homepage plus one inside section homepage, one information page and one state homepage to start).
Once our executive have selected and approved the winning concept, we will offer you the opportunity to complete all other sections of the site including a variety of flash banners and other visual section headings, advertising and promotional pieces not only for the central tollandvesper.com.au site, but for all of the state sites (8), which will replicate the central site with mainly banner and advertising changes. We will look after content entry.
This project will grow into quite a large opportunity for the right designer with ongoing design elements in the form of flash banners, banner ads, newsletter and other emarketing designs, plus related blogs and product sites required over time.
We will provide you with a flexible wireframe architecture from which to work, along with conceptual content and imagery where available (feel free to use stock images wherever necessary). If you need something else, just ask!
Deadline
Unfortunately, we need you to work to a ridiculously tight deadline on the concept design, due to a pending executive meeting (where we are committed to making a decision on the approved concept). We need your designs to be submitted by 3/11/2009. The good news is that we can get started on the full project reasonably quickly following the first deadline.
Some of our competitors:
www.bellcastrow.com.au
www.lunden.com.au
www.quillam.com.au
www.zrt.com.au
www.vne.com.au
www.oscarmeade.com.au
www.tavro.com.au
www.pellingtrust.com.au
www.gzt.com.au
www.dorvi.com
You'll need to contact me at marenb@tollandvesper.net so that I can give you access to the resources you'll need to get the conceptual design job done. Just send me a quick note letting me know that you're interested in the contest.
Updates
Hello to all Tolland Vesper website redesign competitors!
A quick hello to all our competitors!
Thank you for submitting your fabulous designs... I will be looking at each of them tomorrow (PM) and will provide you with individual feedback and in some cases, requests for minor modifications prior to our Executive presentation on the 6th. Once again, I do apologise for the delay in my response and the rush required at your end.
Many thanks
Maren
Hello,
I have extended the deadline via ArtQuarry to enable you to make the requested changes and get them back to me asap TODAY!
Although I only extended the deadline by 1 day, it is now showing as almost 2 days left. This is not the case. I MUST have your revised designs as soon as possible TODAY.
Many thanks for your great work!
Maren
Hi!
Hello Art Quarry Contestants!
I'm terribly sorry about the delay... still waiting on the OK from our Senior Executive members on which design we will pursue. I am chasing an answer and will get back to you as soon as possible.
Many thanks for your patience.
Maren
Target Market(s)
Our primary target is the mid-size SME marketplace with turnover $5 - $50mil (CFO, COO, MD, GM - ie, Senior Executives) plus High Net worth individuals and high quality staff.
Tolland Vesper's target market are clients who have (and are) invested in their businesses and/or themselves but now need our assistance to grow and develop further.
They need accountants and advisers who can deliver more than the fundamentals. Our clients are defined by an attitude that motivates them to seek out opportunities while putting the structures in place to ensure the security of their futures.
Number of Pages Required
4 pages
Requirements
Must have
- Designs must be clean and uncluttered whilst maintaining a slick and professional yet approachable look and feel.
The corporate logo must be used and unchanged.
A series of attractive, text based flash animated banners will be required to highlight our key messaging
All of the page components as outlined in the concept design provided are required (although layout and other suggested modifications are welcomed).
As noted earlier, you need to contact me at marenb@tollandvesper.net so that I can give you access to the resources you''ll need to get the conceptual design job done. Just send me a quick note letting me know that you''re interested in the content.
Nice to have
- If possible (although not absolutely necessary), consideration should be made regarding tying in our NZ member firm''s site design at www.tollandvesper.co.nz (which will not change) along with www.caldrewglobal.com. Although we don''t wish to replicate either of these designs, it would be nice to somehow connect them visually in some way. Certainly the site map at the bottom of the page (like the NZ site) must be maintained.
If you want to chat through the brief you are welcome to call or IM me on skype: maren.belitsos
Should not have
- images of abacus''s!

```html
<!DOCTYPE html>
<html lang="en">
<head>
<meta charset="utf-8">
<title>Tolland Vesper – Accountants &amp; Business Advisors</title>
<link rel="stylesheet" href="https://fonts.googleapis.com/css2?family=Jost:wght@300;400;500;600&family=Open+Sans:wght@400;600;700&family=Archivo+Black&display=swap">
<style>
:root{
  --ink:#2a323e;
  --band:#2a323e;
  --brand-blue:#2b4a9b;
  --text:#2e3440;
  --muted:#5a6270;
  --white:#ffffff;
  --rule:#bdbdbd;
  --side-edge:#c4c4c4;
  --side-fade:#cfcfcf;
}
*{box-sizing:border-box;margin:0;padding:0}
html,body{width:1060px;height:1200px;overflow:hidden;background:var(--white)}
body{position:relative;font-family:"Open Sans",Verdana,sans-serif;color:var(--text)}
.abs{position:absolute}
.futura{font-family:"Jost","Futura",sans-serif}

/* header */
.brand-mark{left:48px;top:30px;width:34px;height:34px;border-radius:50%;background:var(--brand-blue)}
.brand-divider{left:119px;top:12px;width:1px;height:58px;background:var(--ink)}
.brand-name{left:134px;top:24px;font:500 21px/1 "Jost",sans-serif;color:var(--ink)}
.brand-tag{left:269px;top:29px;font:300 16px/1 "Jost",sans-serif;color:var(--brand-blue)}
.search-label{left:752px;top:42px;font:300 15px/1 "Jost",sans-serif;color:var(--ink)}
.search-box{left:795px;top:40px;width:188px;height:24px;border:1px solid var(--ink);background:var(--white)}
.search-btn{left:982px;top:40px;width:23px;height:24px;background:var(--ink)}
.nav{left:47px;top:80px;display:flex;gap:0;font:300 14.5px/1 "Jost",sans-serif;color:var(--ink)}
.nav span{position:absolute;white-space:nowrap}
.nav-active{left:37px;top:98px;width:53px;height:8px;background:var(--white);border-radius:0 0 3px 3px;z-index:2}

/* hero band */
.hero{left:0;top:100px;width:1060px;height:230px;background:var(--band)}
.photo{background:linear-gradient(135deg,#c9b8a3,#8e7a66 55%,#3e3a3a)}
.photo.p2{background:linear-gradient(135deg,#8aa0c4,#3d4a66 50%,#b86a3a)}
.photo.p3{background:linear-gradient(135deg,#f4f1ec,#d8c8b6 60%,#b9896a)}
.case h3{font:500 22px/1 "Jost",sans-serif;color:var(--white)}
.case p{margin-top:6px;font:300 9px/11.2px "Jost",sans-serif;color:#e6e8ec;white-space:nowrap}
.case .more{margin-top:12px}
.feature-title{left:753px;top:148px;font:600 35px/1 "Jost",sans-serif;color:var(--white);letter-spacing:-.3px}
.feature-text{left:753px;top:190px;font:300 14.8px/17px "Jost",sans-serif;color:#e6e8ec;white-space:nowrap}
.feature-more{left:753px;top:257px;font:300 15px/1 "Jost",sans-serif;color:#e6e8ec}
.tabs{left:753px;top:316px;display:flex;gap:1px}
.tabs span{width:41px;height:14px;background:var(--white);border-radius:3px 3px 0 0;font:600 13px/16px "Jost",sans-serif;text-align:center;color:var(--ink)}

/* sidebar */
.sidebar{left:735px;top:330px;width:325px;height:565px;border-left:3px solid var(--side-edge);background:linear-gradient(to bottom,var(--white) 0,var(--white) 74%,var(--side-fade) 100%)}
.side-menu{left:763px;top:346px;font:400 14px/17.8px "Archivo Black",sans-serif;color:var(--ink);letter-spacing:.4px}
.side-text{left:763px;top:558px;font:400 13px/15.3px "Open Sans",Verdana,sans-serif;color:var(--ink);white-space:nowrap}
.side-text p{margin-bottom:15.3px}

/* articles */
.headline{font:500 26px/29px "Jost",sans-serif;color:var(--ink);letter-spacing:-.3px;white-space:nowrap}
.body{font:400 13px/15.2px "Open Sans",Verdana,sans-serif;color:var(--ink);white-space:nowrap}
.article-photo{left:22px;top:519px;width:283px;height:131px;background:linear-gradient(90deg,#6b7a5a,#c8b24a 35%,#3a4a6a 70%,#2c3140)}
.divider{left:52px;top:680px;width:580px;height:2px;background:var(--rule)}
.equity p{margin-bottom:15.2px}

/* footer */
.footer{left:0;top:895px;width:1060px;height:242px;background:var(--band)}
.foot-col{top:906px;font:400 9.5px/21.2px "Open Sans",Verdana,sans-serif;color:#e9ebee;white-space:nowrap}
.foot-col h4{font-weight:700;font-size:9.5px;letter-spacing:.3px;color:var(--white)}
.legal-links{left:26px;top:1143px;font:300 11px/1 "Jost",sans-serif;color:var(--muted);white-space:nowrap}
.legal-links span{margin-right:19px}
.legal-text{left:26px;top:1156px;font:300 9.6px/12px "Jost",sans-serif;color:var(--muted);white-space:nowrap}
</style>
</head>
<body>

<!-- header -->
<div class="abs brand-mark"></div>
<div class="abs brand-divider"></div>
<div class="abs brand-name">Tolland Vesper</div>
<div class="abs brand-tag">Accountants &amp; Business Advisors</div>
<div class="abs search-label">Search</div>
<div class="abs search-box"></div>
<div class="abs search-btn">
  <svg width="23" height="24" viewBox="0 0 23 24"><path d="M9 6l6 6-6 6" fill="none" stroke="#fff" stroke-width="1.6"/></svg>
</div>
<nav class="abs nav" style="left:0;top:80px;width:600px;height:20px">
  <span style="left:47px">Home</span>
  <span style="left:95px">About</span>
  <span style="left:143px">Services</span>
  <span style="left:202px">Our Network</span>
  <span style="left:292px">Infotelligence</span>
  <span style="left:381px">Contact</span>
  <span style="left:438px">Login</span>
</nav>

<!-- hero -->
<section class="abs hero"></section>
<div class="abs nav-active"></div>

<div class="abs photo" style="left:45px;top:121px;width:172px;height:112px" role="img" aria-label="Photo of a smiling business team"></div>
<div class="abs case" style="left:45px;top:241px">
  <h3>Case Study 1</h3>
  <p>Case Study: "Sed ut perspiciatis unde omnis iste<br>natus error sit voluptatem accusantium doloremque<br>laudantium, totam rem aperiam, eaque ipsa quae</p>
  <p class="more">Read more</p>
</div>

<div class="abs photo p2" style="left:281px;top:117px;width:165px;height:112px" role="img" aria-label="Photo of business people walking through a glass building"></div>
<div class="abs case" style="left:281px;top:238px">
  <h3>Case Study 2</h3>
  <p>Case Study: "Sed ut perspiciatis unde omnis iste<br>natus error sit voluptatem accusantium doloremque<br>laudantium, totam rem aperiam, eaque ipsa quae</p>
  <p class="more">Read more</p>
</div>

<div class="abs photo p3" style="left:507px;top:117px;width:166px;height:112px" role="img" aria-label="Photo of a businesswoman in front of colleagues"></div>
<div class="abs case" style="left:507px;top:238px">
  <h3>Case Study 3</h3>
  <p>Case Study: "Sed ut perspiciatis unde omnis iste<br>natus error sit voluptatem accusantium doloremque<br>laudantium, totam rem aperiam, eaque ipsa quae</p>
  <p class="more">Read more</p>
</div>

<h2 class="abs feature-title">Our Network.</h2>
<div class="abs feature-text">Case Study: "Sed ut perspiciatis unde omnis iste<br>natus error sit voluptatem accusantium doloremque<br>laudantium, totam rem aperiam, eaque ipsa quae</div>
<div class="abs feature-more">Read more</div>
<div class="abs tabs"><span>1</span><span>2</span><span>3</span><span>4</span><span>5</span></div>

<!-- sidebar -->
<aside class="abs sidebar"></aside>
<div class="abs side-menu">CONTACT<br>STRUCTURE<br>CREED<br>MEMBER FIRMS<br>LEADERS<br>NETWORK<br>COMMUNITY<br>NEWS &amp; EVENT</div>
<div class="abs side-text">
  <p>A key issue introduction text goes here<br>and links through to a webpage in the<br>site. Can be a continuation of the article<br>or a link to a general section of the site.</p>
  <p>It will not be more than 2 or 3 sentences<br>to tease the visitor to click on the link.</p>
  <p>It must include much more white space<br>(air) between the seperate pieces than<br>this mockup actually shows.</p>
  <p>Click here to find out more</p>
</div>

<!-- articles -->
<h2 class="abs headline" style="left:22px;top:346px">The threat to businesses<br>with unrelated shareholders</h2>
<div class="abs body" style="left:22px;top:407px">If you are in business with shareholders that<br>are not related to you, your business faces a<br>potentially major and costly threat, if one of<br>your fellow shareholders dies or becomes per-<br>manently disabled. Good planning through<br>buy/sell agreements and appropriate insur-<br>ance can make all the difference.</div>
<div class="abs article-photo" role="img" aria-label="Photo of a business meeting around a table"></div>

<h2 class="abs headline" style="left:363px;top:346px">Is good cash flow management<br>enough to save your business?</h2>
<div class="abs body" style="left:363px;top:407px">An enticing but relevant image related to a selected<br>key issue goes here (to change as the market dic-<br>tates). Image should not overpower the headline<br>below. It will include a 'word' that represents an<br>issue type. We will need a library of images to be<br>used as required. Including: Innovation, Strategy,<br>Assurance, Advice, Hot Issue, Important to know!, In<br>the News, Upcoming Event, Hot News, In the Know,<br>Business Scruples - Q&amp;As, Business Briefing, To your<br>good Wealth, In the media, You're Invited, Don't miss<br>our Whitepaper!, Noteable achievement, In the com-<br>munity, On your side,&nbsp; (and more over time)<br><br>Q&amp;As, Business Briefing, To your good Wealth, In the<br>media, You're Invited, Don't miss our Whitepaper!,<br>Noteable achievement, In the community.</div>

<div class="abs divider"></div>

<h2 class="abs headline" style="left:18px;top:700px">Are you ready for private equity?</h2>
<div class="abs body equity" style="left:18px;top:740px">
  <p>A key issue introduction text goes here and links through to a webpage in the site. Can be a continuation<br>of the article or a link to a general section of the site.</p>
  <p>It will not be more than 2 or 3 sentences to tease the visitor to click on the link.</p>
  <p>It must include much more white space (air) between the seperate pieces than this mockup actually<br>shows.</p>
  <p>Click here to find out more</p>
</div>

<!-- footer -->
<footer class="abs footer"></footer>
<div class="abs foot-col" style="left:38px"><h4>ABOUT US</h4>Our Clients<br>Our Difference<br>Our Directors<br>Our Associations</div>
<div class="abs foot-col" style="left:227px"><h4>SERVICES</h4>Beyond the numbers<br>Business Advisory<br>ServicesTaxation<br>Audit &amp; Assurance<br>Business Improvement</div>
<div class="abs foot-col" style="left:406px"><h4>CAREERS</h4>Tools For Accountants<br>Tools For Businesses</div>
<div class="abs foot-col" style="left:573px"><h4>TOOLS</h4>Opportunities<br>Careers<br>Current Vacancies<br>Apply Now</div>
<div class="abs foot-col" style="left:726px"><h4>CONTACT US</h4>Kestrel Bay<br>PH: +64 9 555 0142<br>Email: office@tollandvesper.co.nz<br>Marlow Heights<br>PH: +64 9 555 0187<br>Email: info@tollandvesper.co.nz</div>
<div class="abs foot-col" style="left:925px"><h4>EVENTS</h4>Privacy Policy<br>Disclaimer</div>

<div class="abs legal-links"><span>Copyright</span><span>Privacy</span><span>Disclaimer</span><span>Subscribe</span><span>Site Manager</span><span>Links</span><span>RSS and other Social media links</span></div>
<div class="abs legal-text">Tolland Vesper refers to the network of member firms of Tolland Vesper Group, each of which is a separate and independent legal entity. Tolland Vesper Group is the principal governance entity of the global Tolland Vesper Network and does not provide<br>any services to clients. Services are provided by Tolland Vesper Group member firms. Each of Tolland Vesper Group and its member firms is a separate legal entity and has no liability for another such entity's acts or omissions. Certain content on this site<br>may have been prepared by one or more Tolland Vesper Group member firms. Limited Liability by a scheme approved under Professional Standards Legislation.</div>

</body>
</html>
```